New Stationary for our business

We are a gift business and would like to create a new corporate image with new stationary and design.

We would like a Classic Corporate look with a touch of Flair.

We would need:
Envelopes
Letter Head
Business Cards
With Comp Slips
Note Pads
Etc...

Our details are:

Basket Haven Pty Ltd
518 Tallow Street, Fernmead, Victoria, 3071
1800 742 918
www.baskethaven-demo.com.au
sales@baskethaven-demo.com.au

ABN: 58 603 214 796

Target Market(s)

Corporate Look

Industry/Entity Type

Marketing

Contact Information for Business Card

Basket Haven Pty Ltd
1800 742 918
518 Tallow Street
Fernmead 3071
Victoria Australia

Darren Pelluso - Managing Director
darren.pelluso@baskethaven-demo.com.au
0413 587 120

Logo Text

Basket Haven - The Gift Specialists

Colors

Designer to choose colors to be used in the design.

Requirements
Must have
• Look and Feel upmarket and exclusive

```html
<!DOCTYPE html>
<html lang="en">
<head>
<meta charset="utf-8">
<title>Basket Haven – Business Card</title>
<link rel="stylesheet" href="https://fonts.googleapis.com/css2?family=Roboto:wght@400;500&display=swap">
<style>
  :root {
    --backdrop: #a3a3a3;
    --card-dark: #000000;
    --card-light: #f4f4f4;
    --ink-light: #ffffff;
    --ink-dark: #111111;
    --ink-muted: #555555;
    --rule: #c9c9c9;
  }
  * { margin: 0; padding: 0; box-sizing: border-box; }
  html, body { width: 1200px; height: 960px; overflow: hidden; }
  body {
    position: relative;
    background: var(--backdrop);
    font-family: "Roboto", Arial, sans-serif;
  }
  .card {
    position: absolute;
    width: 600px;
    height: 345px;
    box-shadow: 0 3px 6px rgba(0,0,0,0.35);
  }
  .card--front {
    left: 322px; top: 108px;
    background: var(--card-dark);
    color: var(--ink-light);
  }
  .card--back {
    left: 320px; top: 492px;
    background: var(--card-light);
    color: var(--ink-dark);
  }
  .brand-name {
    position: absolute;
    font-weight: 400;
    white-space: nowrap;
  }
  .card--front .brand-name {
    left: 0; right: 0; top: 150px;
    text-align: center;
    font-size: 40px;
    color: var(--ink-light);
  }
  .card--front .web {
    position: absolute;
    left: 0; right: 0; top: 280px;
    text-align: center;
    font-size: 14px;
    letter-spacing: 3px;
  }
  .card--back .brand-name {
    left: 42px; top: 146px;
    width: 270px;
    text-align: center;
    font-size: 32px;
    color: var(--ink-dark);
  }
  .divider {
    position: absolute;
    left: 328px; top: 62px;
    width: 1px; height: 218px;
    background: var(--rule);
  }
  .details {
    position: absolute;
    left: 346px; top: 78px;
  }
  .person-name {
    font-size: 20px;
    font-weight: 500;
    line-height: 26px;
    color: var(--ink-dark);
  }
  .person-role {
    font-size: 14px;
    font-weight: 500;
    line-height: 20px;
    color: #444;
    margin-bottom: 12px;
  }
  .address {
    font-size: 14px;
    line-height: 18px;
    color: var(--ink-muted);
    font-style: normal;
    margin-bottom: 10px;
  }
  .contact-list { list-style: none; }
  .contact-list li {
    display: flex;
    align-items: center;
    font-size: 14px;
    line-height: 19px;
    color: var(--ink-muted);
  }
  .contact-list svg {
    width: 12px; height: 12px;
    margin-right: 10px;
    fill: var(--ink-dark);
  }
</style>
</head>
<body>

  <section class="card card--front">
    <div class="brand-name">Basket Haven</div>
    <div class="web">www.baskethaven-demo.com.au</div>
  </section>

  <section class="card card--back">
    <div class="brand-name">Basket Haven</div>
    <div class="divider"></div>
    <div class="details">
      <div class="person-name">LEON HARTLEY</div>
      <div class="person-role">CEO/FOUNDER</div>
      <address class="address">
        Basket Haven Pty Ltd<br>
        518 Tallow Street<br>
        Fernmead, Victoria, 3071
      </address>
      <ul class="contact-list">
        <li>
          <svg viewBox="0 0 12 12" aria-hidden="true"><path d="M2.4 0.6 L4.2 2.9 L3.2 4.2 C3.8 5.6 6.4 8.2 7.8 8.8 L9.1 7.8 L11.4 9.6 L10.2 11.4 C6 11.6 0.4 6 0.6 1.8 Z"/></svg>
          1800 742 918
        </li>
        <li>
          <svg viewBox="0 0 12 12" aria-hidden="true"><path d="M0.5 2.5 H11.5 V9.5 H0.5 Z M1.3 3 L6 6.6 L10.7 3 Z" fill-rule="evenodd"/></svg>
          sales@baskethaven-demo.com.au
        </li>
        <li>
          <svg viewBox="0 0 12 12" aria-hidden="true"><circle cx="6" cy="6" r="5.5"/><path d="M3 4 C4 3 5 4.5 4.5 5.5 C4 6.5 5.5 7 5 8.5 L3.5 9 Z M7 2 C8 3 9 3 9.5 4.5 L8 5 Z" fill="#f4f4f4"/></svg>
          www.baskethaven-demo.com.au
        </li>
      </ul>
    </div>
  </section>

</body>
</html>
```